Business Card Design Project: Classically Trained Singer and Voice Teacher

I am a classically trained singer that performs in Opera and Musical Theater and also teaches private voice lessons in those fields. I am looking for a business card that I can give to casting directors and colleagues, as well as to people who are interested in taking voice lessons from me.

This is sort of like an actors business card so I want my headshot and name to be the main focus.

I was kind of thinking of having the business card be horizontal with my headshot photo on the front taking up roughly half and my information on the same side, and perhaps my name again on the back or some form of my initials. But I am totally open to other options for layout.I would prefer to have a double sided business card, but once again, its not essential.

I am looking for it to look and feel elegant artistic and professional, without looking feminine.

Because of the colors of my headshot I would imagine that it would be predominantly brown and white, but I am totally open to other approaches.feel totally free to crop my headshot so that it fits better into your overall design and layout.

It is highly likely that I will ask the winner of the design to create a flyer for marketing my voice lessons with a similar look.

If you have any questions or clarifications, please feel free to ask.

Target Market(s)

Opera and Musical theater casting directors, colleagues; potential voice lesson students

Industry/Entity Type

Marketing

Requirements
Must have
• These must feature prominently:
- (My Headshot (attached))
- Marlow Keating (my name)

These dont need to be as prominent:
- Baritone
- Private Voice Teacher
- Opera and Musical Theater

Contact Info:
Phone: (555) 347-2816
Email: marlkeat@inboxly.example

Nice to have
• Double sided

```html
<!DOCTYPE html>
<html lang="en">
<head>
<meta charset="utf-8">
<title>Marlow Keating – Business Card</title>
<link href="https://fonts.googleapis.com/css2?family=Electrolize&family=Arimo:wght@700&display=swap" rel="stylesheet">
<style>
  :root {
    --page: #ffffff;
    --frame: #2a2420;
    --teal: #6f9893;
    --teal-light: #82aaa4;
    --band: #2f2824;
    --ink: #2a2420;
    --name-light: #ffffff;
    --photo-dark: #4a3a30;
    --photo-mid: #9a8878;
    --photo-light: #e4e2de;
    --back-light: #e6edc6;
    --back-mid: #d3dfa8;
    --back-edge: #bccb8e;
  }
  * { box-sizing: border-box; margin: 0; padding: 0; }
  html, body {
    width: 1140px;
    height: 1200px;
    overflow: hidden;
    background: var(--page);
  }
  .canvas {
    position: relative;
    width: 1140px;
    height: 1200px;
  }
  .card {
    position: absolute;
    left: 180px;
    width: 780px;
    height: 474px;
    border: 8px solid var(--frame);
    border-radius: 26px;
    overflow: hidden;
  }
  .card-front { top: 96px; }
  .card-back { top: 618px; }

  /* Front */
  .headshot {
    position: absolute;
    inset: 0;
    background: linear-gradient(100deg, var(--photo-light) 30%, var(--photo-mid) 62%, var(--photo-dark) 85%, var(--photo-light) 100%);
  }
  .front-shapes {
    position: absolute;
    inset: 0;
    width: 100%;
    height: 100%;
  }
  .front-name {
    position: absolute;
    left: 32px;
    top: 30px;
    font-family: "Electrolize", sans-serif;
    font-weight: 400;
    font-size: 48px;
    line-height: 1.02;
    color: var(--name-light);
  }
  .front-roles {
    position: absolute;
    left: 0;
    width: 346px;
    top: 198px;
    text-align: center;
    font-family: "Electrolize", sans-serif;
    font-size: 23px;
    line-height: 1.18;
    color: var(--ink);
    list-style: none;
  }

  /* Back */
  .back-panel {
    position: absolute;
    inset: 0;
    background: radial-gradient(ellipse at 50% 45%, var(--back-light) 0%, var(--back-mid) 65%, var(--back-edge) 100%);
  }
  .back-name {
    position: absolute;
    left: 0;
    right: 0;
    top: 26px;
    text-align: center;
    font-family: "Electrolize", sans-serif;
    font-weight: 400;
    font-size: 50px;
    line-height: 1.02;
    color: var(--ink);
  }
  .back-contact {
    position: absolute;
    left: 0;
    right: 0;
    top: 366px;
    text-align: center;
    font-family: "Arimo", sans-serif;
    font-weight: 700;
    font-size: 23px;
    line-height: 1.45;
    color: var(--ink);
  }
</style>
</head>
<body>
<main class="canvas">

  <section class="card card-front" aria-label="Card front">
    <div class="headshot" role="img" aria-label="Headshot photograph of Marlow Keating"></div>
    <svg class="front-shapes" viewBox="0 0 764 458" preserveAspectRatio="none" aria-hidden="true">
      <defs>
        <linearGradient id="teal-fill" x1="0" y1="0" x2="1" y2="1">
          <stop offset="0" stop-color="var(--teal-light)"/>
          <stop offset="1" stop-color="var(--teal)"/>
        </linearGradient>
      </defs>
      <path d="M0 0 H375 C350 160 320 330 230 458 H0 Z" fill="var(--band)"/>
      <path d="M0 0 H342 C322 170 290 330 200 458 H0 Z" fill="url(#teal-fill)"/>
    </svg>
    <h1 class="front-name">Marlow<br>Keating</h1>
    <ul class="front-roles">
      <li>Baritone</li>
      <li>Private Voice Teacher</li>
      <li>Opera</li>
      <li>Musical Theater</li>
    </ul>
  </section>

  <section class="card card-back" aria-label="Card back">
    <div class="back-panel" role="img" aria-label="Envelope illustration in soft green tones"></div>
    <h2 class="back-name">Marlow<br>Keating</h2>
    <p class="back-contact">Phone: (555) 347-2816<br>Email: marlkeat@inboxly.example</p>
  </section>

</main>
</body>
</html>
```